Website refresh for HollowbrookByteworks.com

I need a new fresh website with all of the information contained in hollowbrookbyteworks.com. The website needs to be built on the wix platform as it handles my booking, calendar and email marketing. The imperative pages are Home, About, Services, Clients and Testimonials. The other pages I can recreate based on the design chosen.

Industry/Entity Type

IT Services

Coding

Coded - Design and coding required

Number of Pages Required

5+ page

Font styles to use
Serif

Colors
00AB8E
00BBA5
67D7C9
C6EFE9
E9F9F6

Requirements
Must have
• I will need to be able to edit the document using the Wix WYSIWYG platform.
Nice to have
• See plovrenta.com for a look and feel.
Should not have
• n/a

```html
<!DOCTYPE html>
<html lang="en">
<head>
<meta charset="utf-8">
<title>Hollowbrook Byteworks – On-Site Computer Support</title>
<link rel="stylesheet" href="https://fonts.googleapis.com/css2?family=Montserrat:wght@500;600;700&family=Open+Sans:wght@400;600&display=swap">
<style>
:root{
  --navy:#0c2647;
  --navy-deep:#081a33;
  --teal:#00AB8E;
  --teal-2:#00BBA5;
  --teal-3:#67D7C9;
  --teal-4:#C6EFE9;
  --teal-5:#E9F9F6;
  --forest:#0e6b55;
  --mint-panel:#c9f7d2;
  --card-mint:#eaf8ec;
  --ink:#222;
  --body:#4a4a4a;
  --link:#1a5fb4;
  --star:#f4b400;
  --white:#fff;
}
*{box-sizing:border-box;margin:0;padding:0}
html,body{width:1200px;height:4138px;overflow:hidden}
body{position:relative;background:var(--white);font-family:'Open Sans',sans-serif;color:var(--body)}
.abs{position:absolute}
h2.section-title{font-family:'Montserrat',sans-serif;font-weight:500;font-size:24px;color:var(--ink);text-align:center}
.lead{font-size:13px;line-height:20px;text-align:center;color:var(--body)}
a{color:var(--link);text-decoration:none}

.hero-bg{left:0;top:0;width:1200px;height:700px}
.brand{display:flex;align-items:center;gap:8px;color:var(--white);font-family:'Montserrat',sans-serif;font-weight:700;font-size:14px;line-height:15px}
.brand-mark{width:22px;height:22px;background:var(--teal-2);border-radius:3px}
.nav a{position:absolute;top:34px;color:var(--white);font-size:12.5px;font-weight:600;font-family:'Open Sans',sans-serif}
.nav a.active{color:#19c99a}
.hero-title{left:100px;top:192px;font-family:'Montserrat',sans-serif;font-weight:600;font-size:43px;color:var(--white)}
.hero-text{left:100px;top:255px;width:440px;font-size:13px;line-height:20px;color:#e8eef6}
.btn{display:inline-flex;align-items:center;justify-content:center;border-radius:3px;font-weight:600;font-size:13px}
.btn-light{background:var(--white);color:var(--navy)}
.btn-forest{background:var(--forest);color:var(--white)}

.client{top:1134px;width:137px;height:86px;background:var(--white);box-shadow:0 2px 10px rgba(0,0,0,.12);display:flex;align-items:center;justify-content:center;font-family:'Montserrat',sans-serif;font-weight:600;font-size:14px;text-align:center}

.services-panel{left:100px;top:1320px;width:1000px;height:361px;background:var(--mint-panel);border-radius:16px}
.svc-card{top:1399px;width:209px;height:247px;background:var(--white);border-radius:8px;padding:12px}
.svc-photo{width:185px;height:122px;border-radius:4px}
.svc-card h3{font-family:'Montserrat',sans-serif;font-weight:500;font-size:13px;color:var(--ink);margin-top:14px}
.svc-card p{font-size:12.5px;line-height:20px;color:#6b6b6b;margin-top:6px}

.rec-title{left:100px;top:1756px;font-family:'Montserrat',sans-serif;font-weight:600;font-size:24px;color:var(--white)}
.rec-text{left:100px;top:1808px;width:460px;font-size:12.5px;line-height:20px;color:#e8eef6}

.tile{width:137px;height:127px;background:var(--white);box-shadow:0 2px 12px rgba(0,0,0,.12);border-radius:4px;display:flex;flex-direction:column;align-items:center;padding-top:14px;text-align:center}
.tile svg{width:46px;height:46px;fill:none;stroke:var(--teal);stroke-width:1.6;stroke-linejoin:round;stroke-linecap:round}
.tile span{font-family:'Montserrat',sans-serif;font-weight:500;font-size:11.5px;line-height:15px;color:#333;margin-top:8px;padding:0 8px}

.video-frame{left:241px;top:2746px;width:718px;height:424px;background:var(--white);border-radius:16px;box-shadow:0 2px 14px rgba(0,0,0,.1)}
.video-thumb{left:265px;top:2770px;width:668px;height:375px;border-radius:14px;background:radial-gradient(circle at 55% 45%,#3f9a2e 0%,#1c5a16 45%,#0b2a08 100%)}

.review{top:3373px;width:306px;height:329px;background:var(--card-mint);border-radius:8px;padding:16px 17px}
.stars{color:var(--star);font-size:20px;letter-spacing:1px}
.review p{font-size:12.5px;line-height:20px;color:#555;margin-top:14px}
.reviewer{position:absolute;left:17px;bottom:18px;display:flex;align-items:center;gap:10px;font-size:12.5px;color:#333}
.avatar{width:24px;height:24px;border-radius:50%;background:#1d3f9e;color:var(--white);font-weight:700;font-size:12px;display:flex;align-items:center;justify-content:center}

.footer-line{display:flex;align-items:center;gap:10px;color:var(--white);font-family:'Montserrat',sans-serif;font-weight:500;font-size:14px}
.social{top:4022px;width:24px;height:24px;border-radius:50%;background:var(--white)}
</style>
</head>
<body>

<svg class="abs hero-bg" viewBox="0 0 1200 700" role="img" aria-label="Dark blue photo of a laptop with a glowing support, technical and service illustration">
  <defs>
    <linearGradient id="heroGrad" x1="0" y1="0" x2="1" y2="1">
      <stop offset="0" stop-color="#0a1a30"/>
      <stop offset=".55" stop-color="#143a6a"/>
      <stop offset="1" stop-color="#2a5f96"/>
    </linearGradient>
  </defs>
  <rect width="1200" height="700" fill="url(#heroGrad)"/>
  <polygon points="0,650 599,432 599,448 0,690" fill="var(--teal)"/>
  <polygon points="599,432 1200,652 1200,676 599,448" fill="#3b9ad6"/>
  <polygon points="0,690 599,448 1200,676 1200,700 0,700" fill="#fff"/>
  <g transform="translate(599 427) rotate(45)">
    <rect x="-14" y="-14" width="28" height="28" rx="4" fill="#fff"/>
  </g>
  <polyline points="592,424 599,431 606,424" fill="none" stroke="var(--navy)" stroke-width="3" stroke-linecap="round" stroke-linejoin="round"/>
  <polyline points="592,418 599,425 606,418" fill="none" stroke="var(--navy)" stroke-width="3" stroke-linecap="round" stroke-linejoin="round"/>
</svg>

<header>
  <div class="abs brand" style="left:100px;top:24px"><span class="brand-mark"></span><span>Hollowbrook<br>Byteworks</span></div>
  <nav class="nav">
    <a class="active" style="left:395px">Home</a>
    <a style="left:459px">About</a>
    <a style="left:524px">Media</a>
    <a style="left:588px">Services</a>
    <a style="left:668px">Book Online</a>
    <a style="left:772px">Clients</a>
    <a style="left:843px">We Recommend</a>
    <a style="left:975px">Help Now</a>
  </nav>
  <svg class="abs" style="left:1080px;top:32px" width="20" height="20" viewBox="0 0 20 20"><circle cx="10" cy="10" r="9" fill="none" stroke="#19c99a" stroke-width="1.6"/><circle cx="10" cy="8" r="3" fill="#19c99a"/><path d="M4.5 16c1.5-3 9.5-3 11 0" fill="#19c99a"/></svg>
</header>

<section>
  <h1 class="abs hero-title">Computer Crash ?</h1>
  <p class="abs hero-text">Hollowbrook Byteworks is a Managed Service Provider for numerous small business in the Cedar Valley area.</p>
  <span class="abs btn btn-light" style="left:100px;top:316px;width:176px;height:39px">Call Us : 8335550148</span>
</section>

<section>
  <h2 class="abs section-title" style="left:0;width:1200px;top:627px">A Bit About Us</h2>
  <div class="abs lead" style="left:100px;width:1000px;top:679px">
    <p>Hollowbrook Byteworks is a Managed Service Provider for numerous small business in the Cedar Valley area.&nbsp; Our Remote Managed Services include Server Monitoring and Care, <a>Desktop Monitoring and Care</a> as well as <a>Security Assessments, Optimization and Monitoring</a>.</p>
    <p style="margin-top:13px">We also provide <a>on-site computer</a> (both PC and Laptop) repair and IT Support to small business and residential customers. We specialize in on-site computer repair.</p>
    <p style="margin-top:13px">Whether your computer is infected with a Virus, Spyware, Malware, or you are looking for help managing your small business IT systems, Hollowbrook Byteworks is ready to help you in the Cedar Valley area.</p>
    <p style="margin-top:13px">Hollowbrook Byteworks is a complete on-site computer support and service company. Don't feel the need to disconnect all of your computer's parts and drag them into a store. We'll come to your home or office and fix the problem right in front of you.</p>
    <p style="margin-top:13px">In most cases we can get a technician to you the same day you call. Our prices remain reasonable because we don't have the overhead of a retail store. We are here to serve you in the Cedar Valley area.</p>
  </div>
  <span class="abs btn btn-forest" style="left:511px;top:949px;width:178px;height:40px">Request For More Info</span>
</section>

<section>
  <h2 class="abs section-title" style="left:0;width:1200px;top:1083px">Our Trusted Clients</h2>
  <div class="abs client" style="left:100px;color:#1b7fc4">ORLAN</div>
  <div class="abs client" style="left:273px;color:#666">Pantry Loft</div>
  <div class="abs client" style="left:446px;color:#d42a1f">Kestra Realty</div>
  <div class="abs client" style="left:619px;color:#333">Tidewell Group</div>
  <div class="abs client" style="left:792px;color:#4a6f8a">Stonebrook Health</div>
  <div class="abs client" style="left:965px;color:#555">Prism Glass Inc</div>
</section>

<svg class="abs" style="left:0;top:1380px" width="1200" height="714" viewBox="0 0 1200 714">
  <rect width="1200" height="714" fill="var(--navy)"/>
  <polygon points="0,0 1200,0 1200,40 600,180 0,40" fill="#fff"/>
  <polygon points="0,40 0,54 60,48" fill="var(--teal)"/>
  <polygon points="1200,40 1200,54 1140,48" fill="var(--teal)"/>
</svg>

<section>
  <div class="abs services-panel"></div>
  <h2 class="abs section-title" style="left:100px;width:1000px;top:1346px">Our Services</h2>

  <article class="abs svc-card" style="left:133px;padding-top:20px">
    <div class="svc-photo" role="img" aria-label="Laptops on a repair bench" style="background:linear-gradient(135deg,#6a4a3a,#2b2f38)"></div>
    <h3>Repair &amp; Troubleshooting</h3>
    <p>Our expert technicians come directly to your home or office to provide...</p>
  </article>
  <article class="abs svc-card" style="left:374px">
    <div class="svc-photo" role="img" aria-label="Hands typing on a laptop" style="background:linear-gradient(135deg,#3a5a86,#c9d4e4)"></div>
    <h3>Virus Detection/Removal</h3>
    <p>Does it seem like there's a gremlin inside your computer? Does your co...</p>
  </article>
  <article class="abs svc-card" style="left:615px">
    <div class="svc-photo" role="img" aria-label="Colleagues working at a desk" style="background:linear-gradient(135deg,#d8cfc2,#4a5360)"></div>
    <h3>Web Design</h3>
    <p>Are you still using Mailvane, Postwren or Zephmail as your company email address? ...</p>
  </article>
  <article class="abs svc-card" style="left:856px">
    <div class="svc-photo" role="img" aria-label="Technician working on network equipment" style="background:linear-gradient(135deg,#e6e9ee,#6f7f94)"></div>
    <h3>Network Services</h3>
    <p>Your network is vital to your business. When problems arise, you need...</p>
  </article>
</section>

<section>
  <h2 class="abs rec-title">We Recommend</h2>
  <div class="abs rec-text">
    <p>Over the years, I have found a few companies that I just like working with.&nbsp; Great Products, Great Services, Great Deals.&nbsp; I will list them here.</p>
    <p style="margin-top:20px">The list may change and/or grow over time. Please note: Some of the links below are affiliate links, meaning that, if you choose to use the links below and make a purchase, I may earn a commission, at no cost to you.</p>
  </div>
  <span class="abs btn btn-light" style="left:100px;top:1972px;width:106px;height:38px;color:var(--forest)">Know More</span>
  <div class="abs" role="img" aria-label="Desktop computers, laptop, tablets and phones" style="left:562px;top:1762px;width:546px;height:238px;border-radius:10px;background:linear-gradient(120deg,#c9d2dc 0%,#3d6fb0 55%,#1b2a3e 100%);opacity:.9"></div>
</section>

<section>
  <h2 class="abs section-title" style="left:0;width:1200px;top:2172px">On-Site Tech Support</h2>
  <p class="abs lead" style="left:190px;width:820px;top:2210px">We specialize in providing the computer and network support critical for small and home-based Business and Residential customers to succeed in today's world.</p>

  <div class="abs tile" style="left:100px;top:2281px"><svg viewBox="0 0 40 40"><rect x="5" y="7" width="30" height="20" rx="2"/><path d="M15 33h10M20 27v6M12 20l5-5 4 4 7-7"/></svg><span>Remote Maintenance &amp; Monitoring</span></div>
  <div class="abs tile" style="left:273px;top:2281px"><svg viewBox="0 0 40 40"><circle cx="20" cy="15" r="6"/><path d="M11 15a9 9 0 0 1 18 0M9 34c1-7 21-7 22 0M14 26h12"/></svg><span>PC Support &amp; Installation</span></div>
  <div class="abs tile" style="left:446px;top:2281px"><svg viewBox="0 0 40 40"><path d="M20 5l12 5v9c0 8-5 13-12 16C13 32 8 27 8 19v-9z"/><path d="M15 20l4 4 7-8"/></svg><span>Internet Security</span></div>
  <div class="abs tile" style="left:619px;top:2281px"><svg viewBox="0 0 40 40"><rect x="10" y="4" width="18" height="32" rx="3"/><circle cx="24" cy="22" r="5"/><path d="M17 32h4"/></svg><span>Smart Phone Support</span></div>
  <div class="abs tile" style="left:792px;top:2281px"><svg viewBox="0 0 40 40"><path d="M14 6h12l10 18-6 10H10L4 24z"/><path d="M14 6l10 18M4 24h20"/></svg><span>Hard Drive Back Up</span></div>
  <div class="abs tile" style="left:965px;top:2281px"><svg viewBox="0 0 40 40"><circle cx="20" cy="20" r="15"/><ellipse cx="20" cy="20" rx="6" ry="15"/><path d="M5 20h30M8 12h24M8 28h24"/></svg><span>Networking - Home Office / Business</span></div>

  <div class="abs tile" style="left:100px;top:2446px"><svg viewBox="0 0 40 40"><circle cx="12" cy="12" r="4"/><circle cx="28" cy="12" r="4"/><path d="M5 34V22c0-3 14-3 14 0v12M21 34V22c0-3 14-3 14 0v12M10 8h20"/></svg><span>Consulting</span></div>
  <div class="abs tile" style="left:273px;top:2446px"><svg viewBox="0 0 40 40"><rect x="5" y="6" width="30" height="22" rx="2"/><path d="M15 34h10M20 28v6M12 12h6v6h-6zM22 12h6v6h-6zM12 21h16"/></svg><span>IT Solutions</span></div>
  <div class="abs tile" style="left:446px;top:2446px"><svg viewBox="0 0 40 40"><rect x="14" y="4" width="22" height="14"/><path d="M19 14v-4M24 14V8M29 14v-6"/><circle cx="9" cy="22" r="3"/><circle cx="20" cy="26" r="3"/><circle cx="31" cy="26" r="3"/><path d="M4 34c0-4 10-4 10 0M15 36c0-4 10-4 10 0M26 36c0-4 10-4 10 0"/></svg><span>Training</span></div>
  <div class="abs tile" style="left:619px;top:2446px"><svg viewBox="0 0 40 40"><rect x="5" y="6" width="30" height="22" rx="2"/><path d="M15 34h10M20 28v6"/><circle cx="20" cy="17" r="5"/><path d="M12 11a11 11 0 0 0 0 12M28 11a11 11 0 0 1 0 12"/></svg><span>Remote Support</span></div>
  <div class="abs tile" style="left:792px;top:2446px"><svg viewBox="0 0 40 40"><ellipse cx="18" cy="9" rx="12" ry="4"/><path d="M6 9v20c0 2 5 4 12 4M30 9v9M6 16c0 2 5 4 12 4s12-2 12-4M6 23c0 2 5 4 10 4"/><circle cx="28" cy="28" r="6"/><path d="M26 28l2 2 3-4"/></svg><span>Data Recovery</span></div>
  <div class="abs tile" style="left:965px;top:2446px"><svg viewBox="0 0 40 40"><rect x="5" y="10" width="30" height="20" rx="2"/><path d="M15 36h10M20 30v6"/><circle cx="20" cy="10" r="5"/><path d="M20 2v3M20 15v3M12 10h3M25 10h3"/></svg><span>PC/Laptop Repair</span></div>
</section>

<section>
  <h2 class="abs section-title" style="left:0;width:1200px;top:2667px">Tech Tips</h2>
  <p class="abs lead" style="left:0;width:1200px;top:2702px">Is it safe to use Public Wifi networks?&nbsp; How can you protect yourself.</p>
  <div class="abs video-frame"></div>
  <div class="abs video-thumb" role="img" aria-label="Video thumbnail for the public wifi safety tip"></div>
  <svg class="abs" style="left:561px;top:2920px" width="76" height="76" viewBox="0 0 76 76">
    <circle cx="38" cy="38" r="34" fill="rgba(255,255,255,.15)" stroke="#fff" stroke-width="4"/>
    <polygon points="30,24 54,38 30,52" fill="#fff"/>
  </svg>
</section>

<section>
  <h2 class="abs section-title" style="left:0;width:1200px;top:3266px">Testimonials</h2>
  <p class="abs lead" style="left:190px;width:820px;top:3303px">We have been reviewed on <a>Searchpond</a>, <a>Friendline</a>, <a>Nearvoice</a>, <a>Porchpost</a> and the <a>Fair Trade Council</a> as well as the the ones received personally below.</p>

  <article class="abs review" style="left:100px">
    <div class="stars">★★★★★</div>
    <p>Total, complete confidence and trust - I have used their services for a number of years, for all of my equipment. They are responsive, timely and clearly state any problems with alternative solutions and identification of any risks. Appointments are easy to make, and the technician arrives on time or you get a phone call. They are professional and personable, with all around outstanding service.</p>
    <div class="reviewer"><span class="avatar">M</span>Marla K</div>
  </article>
  <article class="abs review" style="left:446px">
    <div class="stars">★★★★★</div>
    <p>I needed to get a new computer and have my data moved to the new computer. Corwin of Hollowbrook Byteworks came on time and even fixed an error message that I had been getting for 3 years and no one else was able to figure out! He re-programmed my Corvela TV remote, fixed my data storage issue on NetHarbor! It was a wonderful experience!!!</p>
    <div class="reviewer"><span class="avatar">R</span>Rosalind T.</div>
  </article>
  <article class="abs review" style="left:793px">
    <div class="stars">★★★★★</div>
    <p>Our laptop was overheating as the fan was not working and the hinge was broken so it was hard to open or close. Hollowbrook Byteworks came highly recommended and our laptop was fixed in a short time. We have had no problems since it was repaired. Thank you Hollowbrook, you came through for us and if we ever need help again, we will call you.</p>
    <div class="reviewer"><span class="avatar">I</span>Ivo P.</div>
  </article>

  <div class="abs" style="left:527px;top:3732px;width:144px;height:2px;background:#ccc"></div>
  <div class="abs" style="left:527px;top:3731px;width:41px;height:4px;background:var(--forest)"></div>
</section>

<svg class="abs" style="left:0;top:3815px" width="1200" height="323" viewBox="0 0 1200 323">
  <polygon points="0,150 700,10 1200,60 1200,323 0,323" fill="#b3ebe0"/>
  <polygon points="0,160 300,60 700,35 1200,95 1200,323 0,323" fill="var(--teal)"/>
  <polygon points="0,170 300,80 700,55 1200,120 1200,323 0,323" fill="var(--forest)"/>
  <polygon points="0,180 700,70 1200,140 1200,323 0,323" fill="var(--navy-deep)"/>
</svg>

<footer>
  <div class="abs brand" style="left:100px;top:4008px;font-size:22px;line-height:24px;gap:12px"><span class="brand-mark" style="width:32px;height:32px"></span><span>Hollowbrook<br>Byteworks</span></div>

  <div class="abs footer-line" style="left:458px;top:3994px">
    <svg width="22" height="22" viewBox="0 0 22 22"><circle cx="11" cy="11" r="11" fill="#fff"/><path d="M7 6c1-1 2-1 2.5 0l1 2c.3.6 0 1-.5 1.4-.4.3-.4.8 0 1.4.6.9 1.2 1.5 2 2 .6.4 1 .4 1.4 0 .4-.5.8-.8 1.4-.5l2 1c1 .5 1 1.5 0 2.5-1.5 1.5-4 1-6.5-1.5S5.5 7.5 7 6z" fill="var(--navy-deep)"/></svg>
    833-BYTE FIX
  </div>
  <div class="abs footer-line" style="left:458px;top:4036px">
    <svg width="22" height="22" viewBox="0 0 22 22"><circle cx="11" cy="11" r="11" fill="#fff"/><rect x="5.5" y="7" width="11" height="8" rx="1" fill="none" stroke="var(--navy-deep)" stroke-width="1.4"/><path d="M5.5 7.5l5.5 4 5.5-4" fill="none" stroke="var(--navy-deep)" stroke-width="1.4"/></svg>
    Help@Hollowbrookbyteworks.com
  </div>

  <div class="abs" style="left:867px;top:3990px;color:#fff;font-family:'Montserrat',sans-serif;font-weight:500;font-size:14px">On-Site Computer Support</div>
  <span class="abs social" style="left:867px"></span>
  <span class="abs social" style="left:909px"></span>
  <span class="abs social" style="left:951px"></span>
  <span class="abs social" style="left:993px"></span>
  <span class="abs social" style="left:1035px"></span>
  <svg class="abs" style="left:1077px;top:4022px" width="24" height="24" viewBox="0 0 24 24"><circle cx="12" cy="12" r="12" fill="#fff"/><path d="M12 18s-4.5-4.5-4.5-7.5a4.5 4.5 0 0 1 9 0C16.5 13.5 12 18 12 18z" fill="var(--navy-deep)"/><circle cx="12" cy="10.5" r="1.6" fill="#fff"/></svg>

  <p class="abs" style="left:0;width:1200px;top:4098px;text-align:center;color:#d6dde8;font-size:13px">Copyright © 2024 Hollowbrook Byteworks. All rights reserved.</p>
</footer>

</body>
</html>
```